Outstanding but small benefit administration firm serving large clients needs a website redesign

While the content on our current website is fine, when people arrive at our website, they know immediately that it was designed years ago. We are looking for something that can potentially be maintained on a content management system because we would like to hire a google certified expert to help with adwords and they often want to change the website or add meta data. We want the design to be mobile device friendly.

As for our company, we stress data accuracy, client customization and outstanding customer service. All of our competitors are large corporations (TelvarPrine, Doltry, Quimby, PayloomCrest, etc.). When we get a client, they stay with us. So many of our competitors do a horrible job with administration that many companies just think that's the way it is in this industry. We need to change that thinking! There is someone who can do it right at a reasonable price. We have very few out of scope fees. KWT knows how to make the transition from one administrator to us as painless as possible.

We like our current colors. We don't have a lot of time to write additional content.

Target Market(s)

Companies with 5,000 to 50,000 employees

Coding

Coded - Design and coding required

Number of Pages Required

2 page

Font styles to use
Sans Serif

Requirements
Must have
• If everything doesn't fit on one page, please show me what the second page would look like. For example, if there are See More links, what happens?
• We need for people to be able to submit short contact us with their company name as a required field.
• Ideally this website will be put on wordpress or something similar.
• Must be mobile device friendly.
Should not have
• Login, Register, Maps of our location, website search

```html
<!DOCTYPE html>
<html lang="en">
<head>
<meta charset="utf-8">
<title>Kestrel Welfare Trust</title>
<link rel="stylesheet" href="https://fonts.googleapis.com/css2?family=Lato:wght@300;400;700;900&family=Raleway:wght@300;400&family=Signika:wght@400;600&display=swap">
<style>
:root{
  --green:#8cc63f;
  --lime:#c4d84a;
  --lime-dark:#a9bf2f;
  --blue:#4db6e8;
  --ink:#222;
  --text:#444;
  --grey-band:#7b7d80;
  --footer:#2b2b2b;
  --footer-deep:#141414;
  --white:#fff;
}
*{box-sizing:border-box;margin:0;padding:0}
html,body{width:1200px;height:2497px;overflow:hidden}
body{font-family:"Lato",sans-serif;color:var(--text);background:var(--white);position:relative}
a{color:inherit;text-decoration:none}
.section{position:absolute;left:0;width:1200px}

/* header */
.site-header{top:0;height:95px;border-top:3px solid #333;background:var(--white)}
.brand{position:absolute;left:100px;top:24px;display:flex;align-items:center;gap:12px}
.brand-dot{width:40px;height:40px;border-radius:50%;background:var(--green)}
.brand-name{font-size:30px;color:#666;font-weight:400}
.header-contact{position:absolute;top:30px;display:flex;align-items:center;gap:12px;font-size:15px;color:#444}
.header-contact .icon{width:32px;height:32px;border-radius:50%;background:#6b6b6b;display:flex;align-items:center;justify-content:center}
.header-phone{left:703px}
.header-mail{left:862px}

/* nav */
.main-nav{top:95px;height:42px;background:#0e0e0e}
.main-nav a{position:absolute;top:0;height:42px;line-height:42px;color:var(--white);font-size:15px;transform:translateX(-50%);white-space:nowrap}
.main-nav a.active{background:var(--lime);color:#222;width:94px;text-align:center}

/* hero */
.hero{top:137px;height:471px;background:linear-gradient(120deg,#9a9a9a 0%,#d6d6d6 35%,#c4c4c4 60%,#6d6d6d 100%)}
.hero-title{position:absolute;left:98px;top:120px;font-family:"Signika",sans-serif;font-weight:600;font-size:32px;line-height:43px;color:var(--white);text-shadow:0 2px 4px rgba(0,0,0,.45);width:360px}
.hero-arrow{position:absolute;top:190px}
.hero-arrow.prev{left:52px}
.hero-arrow.next{right:52px}

/* welcome */
.welcome{top:608px;height:317px;text-align:center}
.welcome h1{margin-top:52px;font-family:"Raleway",sans-serif;font-weight:400;font-size:36px;color:var(--ink)}
.welcome h1 span{color:var(--green)}
.divider{display:block;margin:6px auto 0}
.welcome p{width:1000px;margin:12px auto 0;font-size:13.5px;line-height:22px;color:#333}
.btn-more{display:inline-block;margin-top:22px;width:130px;height:41px;line-height:41px;background:var(--blue);color:var(--white);font-size:16px;font-weight:700}

/* services */
.services{top:925px;height:467px;background:var(--white)}
.services-band{position:absolute;left:0;top:0;width:1200px;height:360px;background:linear-gradient(160deg,#5e5b57 0%,#8a8783 45%,#6f6c68 100%)}
.section-title{position:absolute;left:0;width:1200px;text-align:center;font-family:"Raleway",sans-serif;font-weight:300;font-size:34px}
.services .section-title{top:45px;color:var(--white)}
.services .divider{position:absolute;left:400px;top:92px}
.service-card{position:absolute;top:150px;width:292px;height:290px;background:var(--white);border:2px solid #ddd;padding:8px}
.service-card.featured{border-color:var(--green)}
.service-photo{width:100%;height:230px}
.service-name{display:flex;align-items:center;gap:10px;margin:16px 0 0 10px;font-family:"Signika",sans-serif;font-size:21px;color:#777}
.service-card.featured .service-name{color:var(--green)}
.service-name i{width:12px;height:12px;border-radius:50%;background:#888;display:block}
.service-card.featured .service-name i{background:var(--green)}

/* testimonials */
.testimonials{top:1392px;height:495px;background:linear-gradient(135deg,#c9dc4e 0%,#bcd143 50%,#c8db4d 100%)}
.testimonials .section-title{top:60px;color:#111;font-family:"Lato",sans-serif;font-weight:400;font-size:32px}
.testimonials .divider{position:absolute;left:362px;top:104px}
.client{position:absolute;top:140px;width:316px;text-align:center}
.avatar{width:80px;height:80px;border-radius:50%;margin:0 auto;border:3px solid var(--white);background:linear-gradient(#8a8a8a,#c9c9c9);box-shadow:0 0 0 2px #999}
.client-name{margin-top:20px;font-size:13px;font-weight:700;color:#222}
.client-role{margin-top:4px;font-size:13px;color:#222}
.quote{position:relative;margin-top:32px;height:124px;background:var(--white);border:1px solid #ccc;box-shadow:0 2px 4px rgba(0,0,0,.2);padding:18px 16px 0 18px;text-align:left;font-size:12.8px;line-height:20px;color:#333}
.quote::before{content:"";position:absolute;left:148px;top:-10px;width:16px;height:16px;background:var(--white);border-left:1px solid #ccc;border-top:1px solid #ccc;transform:rotate(45deg)}
.quote-mark{font-family:Georgia,serif;font-size:22px;line-height:10px;color:#bbb;margin-right:6px;vertical-align:-6px}

/* call back */
.callback{top:1887px;height:283px;background:var(--grey-band);color:var(--white)}
.callback h2{position:absolute;left:100px;top:42px;font-family:"Raleway",sans-serif;font-weight:400;font-size:36px;line-height:44px}
.callback-intro{position:absolute;left:100px;top:148px;width:300px;font-size:13.5px;line-height:21px;color:#e4e4e4}
.form-label{position:absolute;left:460px;top:44px;font-size:14px}
.field{position:absolute;width:307px;height:42px;background:var(--white);border:1px solid #ccc;padding:0 12px;font-family:"Lato",sans-serif;font-size:12px;color:#333}
.field::placeholder{color:#777}
.field-message{width:500px}
.btn-submit{position:absolute;left:973px;top:172px;width:127px;height:42px;background:#050505;color:var(--white);border:0;font-family:"Lato",sans-serif;font-weight:900;font-size:16px;cursor:pointer}
.required-note{position:absolute;left:460px;top:226px;font-size:12px;color:#e4e4e4}

/* footer */
.site-footer{top:2170px;height:277px;background:var(--footer);color:#ddd}
.footer-col{position:absolute;top:40px}
.footer-col h3{font-family:"Raleway",sans-serif;font-weight:400;font-size:21px;color:var(--green);padding-bottom:8px;border-bottom:1px solid #555;display:inline-block;min-width:120px}
.footer-sep{position:absolute;top:40px;width:1px;height:200px;background:#444}
.quick-links{list-style:none;margin-top:12px}
.quick-links li{font-size:13px;line-height:28px;padding-left:12px;position:relative}
.quick-links li::before{content:"";position:absolute;left:0;top:12px;width:4px;height:4px;border-radius:50%;background:var(--green)}
.quick-links li.active{color:var(--green)}
.contact-row{display:flex;gap:12px;margin-top:14px;font-size:13px;line-height:19px}
.contact-row strong{color:var(--green)}
.contact-row svg{flex:none;margin-top:3px}
.social{display:flex;align-items:center;gap:16px;margin-top:14px;font-size:13px;font-weight:700}
.social i{width:28px;height:28px;border-radius:50%;background:var(--lime-dark);display:block}
.footer-mark{position:absolute;left:930px;top:100px;font-size:64px;font-weight:700;color:#555}
.copyright{top:2447px;height:50px;background:var(--footer-deep);color:#ddd;text-align:center;line-height:50px;font-size:13px}
.copyright strong{color:var(--white)}

/* inner page (Why KWT) */
.inner-page{position:absolute;left:0;top:0;width:1200px;height:2497px;background:var(--white);display:none;z-index:10}
.inner-page:target{display:block}
.page-banner{top:137px;height:220px;background:linear-gradient(160deg,#5e5b57 0%,#8a8783 45%,#6f6c68 100%);color:var(--white)}
.page-banner h1{position:absolute;left:100px;top:70px;font-family:"Raleway",sans-serif;font-weight:300;font-size:44px}
.breadcrumb{position:absolute;left:100px;top:135px;font-size:14px;color:#e4e4e4}
.breadcrumb span{color:var(--lime)}
.page-body{top:357px;height:1530px;padding:70px 100px 0}
.page-body h2{font-family:"Raleway",sans-serif;font-weight:400;font-size:32px;color:var(--ink)}
.page-body h2 span{color:var(--green)}
.page-body .divider{margin:10px 0 0}
.page-body p{margin-top:22px;font-size:15px;line-height:26px;color:#333}
.pillars{display:flex;gap:30px;margin-top:50px}
.pillar{flex:1;border:2px solid #ddd;padding:28px 26px}
.pillar h3{display:flex;align-items:center;gap:10px;font-family:"Signika",sans-serif;font-weight:400;font-size:21px;color:var(--green)}
.pillar h3 i{width:12px;height:12px;border-radius:50%;background:var(--green);display:block}
.pillar p{font-size:14px;line-height:23px}
.btn-back{display:inline-block;margin-top:50px;width:150px;height:41px;line-height:41px;text-align:center;background:var(--blue);color:var(--white);font-size:16px;font-weight:700}
</style>
</head>
<body>

<header class="section site-header">
  <div class="brand"><span class="brand-dot"></span><span class="brand-name">Kestrel Welfare Trust</span></div>
  <div class="header-contact header-phone">
    <span class="icon"><svg width="16" height="16" viewBox="0 0 24 24"><path fill="#fff" d="M6.6 10.8c1.4 2.8 3.8 5.1 6.6 6.6l2.2-2.2c.3-.3.7-.4 1-.2 1.1.4 2.3.6 3.6.6.6 0 1 .4 1 1V20c0 .6-.4 1-1 1C10.6 21 3 13.4 3 4c0-.6.4-1 1-1h3.5c.6 0 1 .4 1 1 0 1.3.2 2.5.6 3.6.1.3 0 .7-.2 1z"/></svg></span>
    <span>555-014-2271</span>
  </div>
  <div class="header-contact header-mail">
    <span class="icon"><svg width="16" height="12" viewBox="0 0 16 12"><rect x="0.5" y="0.5" width="15" height="11" fill="none" stroke="#fff"/><path d="M1 1l7 6 7-6" fill="none" stroke="#fff"/></svg></span>
    <span>info@kestrelwelfare.com</span>
  </div>
</header>

<nav class="section main-nav">
  <a class="active" href="#" style="left:120px">Home</a>
  <a href="#why-kwt" style="left:300px">Why KWT</a>
  <a href="#" style="left:471px">Services</a>
  <a href="#" style="left:659px">Technology</a>
  <a href="#" style="left:860px">Case Studies</a>
  <a href="#" style="left:1063px">Contact Us</a>
</nav>

<section class="section hero" role="img" aria-label="Photo from above of business people meeting around a desk with laptop and documents">
  <h2 class="hero-title">We Focus On Large Clients With Complex Plans That Need Both Flexibility And Sophistication</h2>
  <svg class="hero-arrow prev" width="22" height="90" viewBox="0 0 22 90"><path d="M20 2L2 45l18 43" fill="none" stroke="#fff" stroke-width="2"/></svg>
  <svg class="hero-arrow next" width="22" height="90" viewBox="0 0 22 90"><path d="M2 2l18 43L2 88" fill="none" stroke="#fff" stroke-width="2"/></svg>
</section>

<section class="section welcome">
  <h1>Welcome to <span>Kestrel Welfare Trust</span></h1>
  <svg class="divider" width="400" height="12" viewBox="0 0 400 12"><line x1="0" y1="6" x2="188" y2="6" stroke="#999"/><line x1="212" y1="6" x2="400" y2="6" stroke="#999"/><circle cx="200" cy="6" r="4" fill="#4db6e8"/></svg>
  <p>Lorem ipsum dolor sit amet, consectetur adipiscing elit. Sed vitae magna tellus. Aenean ante nunc, semper nec cursus non, rutrum ac eros. Vestibulum mattis justo ac dui bibendum consequat a ac ipsum. Praesent a arcu venenatis, auctor velit eu, suscipit libero. Quisque convallis, leo ac pharetra sagittis, ipsum arcu auctor urna, sit amet cursus risus augue in eros. Duis lacinia nisi vitae leo commodo, non finibus magna maximus. Sed posuere, neque eget bibendum pulvinar, ligula erat suscipit dolor, ut maximus arcu mi et tortor. Quisque imperdiet turpis et ligula mollis ultricies. Mauris lacinia rhoncus odio, at rutrum diam mollis eu.</p>
  <a class="btn-more" href="#why-kwt">Read More</a>
</section>

<section class="section services">
  <div class="services-band" role="img" aria-label="Blurred photo of a pen resting on business papers"></div>
  <h2 class="section-title">OUR SERVICES</h2>
  <svg class="divider" width="400" height="12" viewBox="0 0 400 12"><line x1="0" y1="6" x2="188" y2="6" stroke="#ddd"/><line x1="212" y1="6" x2="400" y2="6" stroke="#ddd"/><circle cx="200" cy="6" r="4" fill="#fff"/></svg>
  <div class="service-card featured" style="left:100px">
    <div class="service-photo" role="img" aria-label="Photo of a hand touching a tablet showing bar charts" style="background:linear-gradient(135deg,#3a5a7a,#b9c9d9 60%,#e9eef3)"></div>
    <div class="service-name"><i></i>Data Accuracy</div>
  </div>
  <div class="service-card" style="left:455px">
    <div class="service-photo" role="img" aria-label="Photo of a business handshake" style="background:linear-gradient(135deg,#2e2e2e,#8d8d8d 55%,#3b3b3b)"></div>
    <div class="service-name"><i></i>Client Customization</div>
  </div>
  <div class="service-card" style="left:808px">
    <div class="service-photo" role="img" aria-label="Photo of smiling support agents wearing headsets" style="background:linear-gradient(135deg,#d9d4cf,#8a7a6e 55%,#3f3a37)"></div>
    <div class="service-name"><i></i>Customer Service</div>
  </div>
</section>

<section class="section testimonials">
  <h2 class="section-title">CLIENTS TESTIMONIALS</h2>
  <svg class="divider" width="476" height="12" viewBox="0 0 476 12"><line x1="0" y1="6" x2="226" y2="6" stroke="#333"/><line x1="250" y1="6" x2="476" y2="6" stroke="#333"/><circle cx="238" cy="6" r="4" fill="#111"/></svg>
  <div class="client" style="left:100px">
    <div class="avatar" role="img" aria-label="Portrait photo of the client"></div>
    <div class="client-name">Mr Arlen Vosk</div>
    <div class="client-role">Director, Lorem Ipsum</div>
    <div class="quote"><span class="quote-mark">&ldquo;</span>Lorem ipsum dolor sit amet, consectetur adipiscing elit. Sed vitae magna tellus. Aenean ante nunc, semper nec cursus non, rutrum ac eros. Vestibulum mattis justo ac dui.</div>
  </div>
  <div class="client" style="left:442px">
    <div class="avatar" role="img" aria-label="Portrait photo of the client"></div>
    <div class="client-name">Miss Tessa Marlow</div>
    <div class="client-role">Director, Lorem Ipsum</div>
    <div class="quote"><span class="quote-mark">&ldquo;</span>Lorem ipsum dolor sit amet, consectetur adipiscing elit. Sed vitae magna tellus. Aenean ante nunc, semper nec cursus non, rutrum ac eros. Vestibulum mattis justo ac dui.</div>
  </div>
  <div class="client" style="left:785px">
    <div class="avatar" role="img" aria-label="Portrait photo of the client"></div>
    <div class="client-name">Mr Dorian Pell</div>
    <div class="client-role">Director, Lorem Ipsum</div>
    <div class="quote"><span class="quote-mark">&ldquo;</span>Lorem ipsum dolor sit amet, consectetur adipiscing elit. Sed vitae magna tellus. Aenean ante nunc, semper nec cursus non, rutrum ac eros. Vestibulum mattis justo ac dui.</div>
  </div>
</section>

<section class="section callback">
  <h2>Request<br>A Call Back</h2>
  <p class="callback-intro">Duis autem vel eum iriure dolormi opl inmokl hendi rerit in vulpu tateml velitm essemol mo molestiel conseqb uat, velmi illum dolor eokf no atn nulla more facilisis</p>
  <form class="callback-form" action="#" method="post">
    <div class="form-label">Please fill up bellow form</div>
    <input class="field" style="left:460px;top:72px" type="text" name="name" placeholder="Name" aria-label="Name">
    <input class="field" style="left:793px;top:72px" type="text" name="company" placeholder="Company Name *" aria-label="Company name" required>
    <input class="field" style="left:460px;top:122px" type="tel" name="phone" placeholder="Phone" aria-label="Phone">
    <input class="field" style="left:793px;top:122px" type="email" name="email" placeholder="Email" aria-label="Email">
    <input class="field field-message" style="left:460px;top:172px" type="text" name="message" placeholder="Message" aria-label="Message">
    <button class="btn-submit" type="submit">SUBMIT</button>
    <div class="required-note">* Required field</div>
  </form>
</section>

<footer class="section site-footer">
  <div class="footer-col" style="left:100px">
    <h3>Quick Links</h3>
    <ul class="quick-links">
      <li class="active">Home</li><li>Why KWT</li><li>Services</li><li>Technology</li><li>Case Studies</li><li>Contact Us</li>
    </ul>
  </div>
  <div class="footer-sep" style="left:272px"></div>
  <div class="footer-col" style="left:333px">
    <h3>Contact Details</h3>
    <div class="contact-row"><svg width="12" height="16" viewBox="0 0 12 16"><path d="M6 0C2.7 0 0 2.6 0 5.8 0 10 6 16 6 16s6-6 6-10.2C12 2.6 9.3 0 6 0zm0 8a2.2 2.2 0 110-4.4A2.2 2.2 0 016 8z" fill="#8cc63f"/></svg><div><strong>Kestrel Welfare Trust</strong><br>4120 Alder Ridge Rd<br>Brookfield, MI 48000</div></div>
    <div class="contact-row"><svg width="14" height="14" viewBox="0 0 24 24"><path fill="#8cc63f" d="M6.6 10.8c1.4 2.8 3.8 5.1 6.6 6.6l2.2-2.2c.3-.3.7-.4 1-.2 1.1.4 2.3.6 3.6.6.6 0 1 .4 1 1V20c0 .6-.4 1-1 1C10.6 21 3 13.4 3 4c0-.6.4-1 1-1h3.5c.6 0 1 .4 1 1 0 1.3.2 2.5.6 3.6.1.3 0 .7-.2 1z"/></svg><div>555-014-2271</div></div>
    <div class="contact-row"><svg width="14" height="14" viewBox="0 0 14 14"><rect x="2" y="0" width="10" height="4" fill="#8cc63f"/><rect x="0" y="5" width="14" height="6" fill="#8cc63f"/><rect x="3" y="9" width="8" height="5" fill="#8cc63f"/></svg><div>555-014-2284</div></div>
    <div class="contact-row"><svg width="14" height="10" viewBox="0 0 16 12"><rect x="0.5" y="0.5" width="15" height="11" fill="none" stroke="#8cc63f"/><path d="M1 1l7 6 7-6" fill="none" stroke="#8cc63f"/></svg><div>info@kestrelwelfare.com</div></div>
  </div>
  <div class="footer-sep" style="left:612px"></div>
  <div class="footer-col" style="left:670px">
    <h3>Follow Us</h3>
    <div class="social"><i></i>Like Us</div>
    <div class="social"><i></i>Follow Us</div>
    <div class="social"><i></i>Connect Us</div>
    <div class="social"><i></i>Add to Circle</div>
  </div>
  <div class="footer-sep" style="left:882px"></div>
  <div class="footer-mark">KWT</div>
</footer>

<div class="section copyright">Copyright © 2016 <strong>Kestrel Welfare Trust.</strong> All rights reserved.</div>

<!-- second page: opened by "Read More" / "Why KWT" -->
<div class="inner-page" id="why-kwt">
  <header class="section site-header">
    <div class="brand"><span class="brand-dot"></span><span class="brand-name">Kestrel Welfare Trust</span></div>
    <div class="header-contact header-phone">
      <span class="icon"><svg width="16" height="16" viewBox="0 0 24 24"><path fill="#fff" d="M6.6 10.8c1.4 2.8 3.8 5.1 6.6 6.6l2.2-2.2c.3-.3.7-.4 1-.2 1.1.4 2.3.6 3.6.6.6 0 1 .4 1 1V20c0 .6-.4 1-1 1C10.6 21 3 13.4 3 4c0-.6.4-1 1-1h3.5c.6 0 1 .4 1 1 0 1.3.2 2.5.6 3.6.1.3 0 .7-.2 1z"/></svg></span>
      <span>555-014-2271</span>
    </div>
    <div class="header-contact header-mail">
      <span class="icon"><svg width="16" height="12" viewBox="0 0 16 12"><rect x="0.5" y="0.5" width="15" height="11" fill="none" stroke="#fff"/><path d="M1 1l7 6 7-6" fill="none" stroke="#fff"/></svg></span>
      <span>info@kestrelwelfare.com</span>
    </div>
  </header>
  <nav class="section main-nav">
    <a href="#" style="left:120px">Home</a>
    <a class="active" href="#why-kwt" style="left:300px">Why KWT</a>
    <a href="#why-kwt" style="left:471px">Services</a>
    <a href="#why-kwt" style="left:659px">Technology</a>
    <a href="#why-kwt" style="left:860px">Case Studies</a>
    <a href="#why-kwt" style="left:1063px">Contact Us</a>
  </nav>
  <section class="section page-banner" role="img" aria-label="Blurred photo of business papers on a desk">
    <h1>Why KWT</h1>
    <div class="breadcrumb">Home / <span>Why KWT</span></div>
  </section>
  <section class="section page-body">
    <h2>About <span>Kestrel Welfare Trust</span></h2>
    <svg class="divider" width="400" height="12" viewBox="0 0 400 12"><line x1="0" y1="6" x2="188" y2="6" stroke="#999"/><line x1="212" y1="6" x2="400" y2="6" stroke="#999"/><circle cx="200" cy="6" r="4" fill="#4db6e8"/></svg>
    <p>Lorem ipsum dolor sit amet, consectetur adipiscing elit. Sed vitae magna tellus. Aenean ante nunc, semper nec cursus non, rutrum ac eros. Vestibulum mattis justo ac dui bibendum consequat a ac ipsum. Praesent a arcu venenatis, auctor velit eu, suscipit libero. Quisque convallis, leo ac pharetra sagittis, ipsum arcu auctor urna, sit amet cursus risus augue in eros. Duis lacinia nisi vitae leo commodo, non finibus magna maximus.</p>
    <p>Sed posuere, neque eget bibendum pulvinar, ligula erat suscipit dolor, ut maximus arcu mi et tortor. Quisque imperdiet turpis et ligula mollis ultricies. Mauris lacinia rhoncus odio, at rutrum diam mollis eu. Nullam tincidunt, velit ac viverra pretium, nibh tortor posuere massa, sed dictum erat lorem non nisl. Integer eget nisi a metus cursus sodales vel sit amet nunc.</p>
    <div class="pillars">
      <div class="pillar"><h3><i></i>Data Accuracy</h3><p>Lorem ipsum dolor sit amet, consectetur adipiscing elit. Sed vitae magna tellus, aenean ante nunc semper nec cursus.</p></div>
      <div class="pillar"><h3><i></i>Client Customization</h3><p>Lorem ipsum dolor sit amet, consectetur adipiscing elit. Sed vitae magna tellus, aenean ante nunc semper nec cursus.</p></div>
      <div class="pillar"><h3><i></i>Customer Service</h3><p>Lorem ipsum dolor sit amet, consectetur adipiscing elit. Sed vitae magna tellus, aenean ante nunc semper nec cursus.</p></div>
    </div>
    <a class="btn-back" href="#">Back to Home</a>
  </section>
  <footer class="section site-footer">
    <div class="footer-col" style="left:100px">
      <h3>Quick Links</h3>
      <ul class="quick-links">
        <li>Home</li><li class="active">Why KWT</li><li>Services</li><li>Technology</li><li>Case Studies</li><li>Contact Us</li>
      </ul>
    </div>
    <div class="footer-sep" style="left:272px"></div>
    <div class="footer-col" style="left:333px">
      <h3>Contact Details</h3>
      <div class="contact-row"><svg width="12" height="16" viewBox="0 0 12 16"><path d="M6 0C2.7 0 0 2.6 0 5.8 0 10 6 16 6 16s6-6 6-10.2C12 2.6 9.3 0 6 0zm0 8a2.2 2.2 0 110-4.4A2.2 2.2 0 016 8z" fill="#8cc63f"/></svg><div><strong>Kestrel Welfare Trust</strong><br>4120 Alder Ridge Rd<br>Brookfield, MI 48000</div></div>
      <div class="contact-row"><svg width="14" height="14" viewBox="0 0 24 24"><path fill="#8cc63f" d="M6.6 10.8c1.4 2.8 3.8 5.1 6.6 6.6l2.2-2.2c.3-.3.7-.4 1-.2 1.1.4 2.3.6 3.6.6.6 0 1 .4 1 1V20c0 .6-.4 1-1 1C10.6 21 3 13.4 3 4c0-.6.4-1 1-1h3.5c.6 0 1 .4 1 1 0 1.3.2 2.5.6 3.6.1.3 0 .7-.2 1z"/></svg><div>555-014-2271</div></div>
      <div class="contact-row"><svg width="14" height="14" viewBox="0 0 14 14"><rect x="2" y="0" width="10" height="4" fill="#8cc63f"/><rect x="0" y="5" width="14" height="6" fill="#8cc63f"/><rect x="3" y="9" width="8" height="5" fill="#8cc63f"/></svg><div>555-014-2284</div></div>
      <div class="contact-row"><svg width="14" height="10" viewBox="0 0 16 12"><rect x="0.5" y="0.5" width="15" height="11" fill="none" stroke="#8cc63f"/><path d="M1 1l7 6 7-6" fill="none" stroke="#8cc63f"/></svg><div>info@kestrelwelfare.com</div></div>
    </div>
    <div class="footer-sep" style="left:612px"></div>
    <div class="footer-col" style="left:670px">
      <h3>Follow Us</h3>
      <div class="social"><i></i>Like Us</div>
      <div class="social"><i></i>Follow Us</div>
      <div class="social"><i></i>Connect Us</div>
      <div class="social"><i></i>Add to Circle</div>
    </div>
    <div class="footer-sep" style="left:882px"></div>
    <div class="footer-mark">KWT</div>
  </footer>
  <div class="section copyright">Copyright © 2016 <strong>Kestrel Welfare Trust.</strong> All rights reserved.</div>
</div>

</body>
</html>
```